i need a template design for online store

hi great designers, i need a template for any online store. But preferably well owned shopping carts. I would be an added advantage if the store is setup for me. I need a mature and attractive colours. My online store deals in electronics.

Industry/Entity Type

Shopping

Number of Pages Required

1 page

```html
<!DOCTYPE html>
<html lang="en">
<head>
<meta charset="utf-8">
<title>Voltline Shop – Online Shop Template</title>
<link href="https://fonts.googleapis.com/css2?family=Open+Sans:ital,wght@0,300;0,400;0,600;0,700;0,800;1,400&display=swap" rel="stylesheet">
<style>
:root{
  --orange:#e2492b;
  --black:#0d0d0d;
  --ink:#1e1e1e;
  --grey-text:#8a8a8a;
  --grey-light:#f1efef;
  --grey-band:#ebebeb;
  --grey-btn:#6d6d6d;
  --white:#ffffff;
  --line:#dddddd;
  --mark-dim:#3a1a14;
}
*{box-sizing:border-box;margin:0;padding:0}
html,body{width:1200px;height:3232px;overflow:hidden}
body{font-family:'Open Sans',Arial,sans-serif;color:var(--ink);background:var(--white);position:relative}

/* top bar */
.topbar{height:47px;background:var(--black);color:#ddd;font-size:11px;position:relative}
.topbar .phone{position:absolute;left:47px;top:15px;display:flex;align-items:center;gap:8px;font-size:15px;color:#eee}
.topbar .links{position:absolute;right:170px;top:16px;display:flex;gap:10px;font-size:11px;letter-spacing:.2px}
.topbar .links .hl{color:var(--orange)}
.topbar .sep{color:#777}
.checkout{position:absolute;right:0;top:0;width:153px;height:47px;background:var(--orange);color:#fff;font-size:12px;font-weight:700;display:flex;align-items:center;justify-content:center;gap:8px}

/* header */
.header{height:115px;position:relative}
.wordmark{position:absolute;left:47px;top:38px;display:flex;align-items:center;gap:12px;font-size:34px;font-weight:700;color:var(--orange);line-height:1;letter-spacing:.5px}
.wordmark i{display:block;width:22px;height:22px;background:var(--orange)}
.search{position:absolute;left:683px;top:44px;display:flex}
.search .field{width:276px;height:34px;border:1px solid #cfcfcf;font-size:11px;color:#999;padding:9px 12px}
.search .btn{width:78px;height:34px;background:#2b2b2b;color:#fff;font-size:11px;font-weight:600;display:flex;align-items:center;justify-content:center}
.currency{position:absolute;left:1051px;top:44px;width:98px;height:34px;border:1px solid #ddd;font-size:11px;color:#aaa;padding:9px 10px}

/* nav */
.nav{height:49px;background:var(--black)}
.nav ul{list-style:none;display:flex;height:49px;width:1106px;margin:0 auto}
.nav li{flex:auto;display:flex;align-items:center;justify-content:center;color:#fff;font-size:11.5px;font-weight:600;border-right:1px solid #2e2e2e}
.nav li:last-child{border-right:none}
.nav li.active{background:var(--orange);flex:0 0 93px}

/* hero */
.hero{height:517px;background:linear-gradient(180deg,#c9c9c9 0%,#ededed 55%,#d6d6d6 100%);position:relative}
.hero .ph-left{position:absolute;left:75px;top:80px;width:345px;height:400px;background:linear-gradient(160deg,#2a2a2a,#5e8a3a 60%,#e8e8e8);border-radius:4px}
.hero .ph-right{position:absolute;left:830px;top:91px;width:370px;height:345px;background:linear-gradient(160deg,#3b3b3b,#1a1a1a 60%,#9a9a9a);border-radius:4px;opacity:.9}
.hero .copy{position:absolute;left:474px;top:112px;width:282px;text-align:center}
.hero .eyebrow{font-style:italic;font-size:19px;color:var(--orange)}
.hero .eyebrow b{color:#333;font-weight:400}
.hero .big{font-size:44px;font-weight:800;color:var(--orange);line-height:1.05;margin-top:6px}
.hero .small{font-size:17px;font-weight:600;color:#222;border-bottom:1px solid #bbb;padding:4px 0 10px}
.hero .summer{font-size:43px;font-weight:700;color:#222;line-height:1.1;margin-top:8px}
.hero .hot{font-size:43px;font-weight:700;color:var(--orange);line-height:1.05;border-bottom:1px solid #bbb;padding-bottom:12px}
.hero .shop{display:inline-block;margin-top:20px;width:146px;height:38px;line-height:38px;background:var(--black);color:#fff;font-size:13px;font-weight:600}
.dots{position:absolute;left:589px;top:633px;display:flex;gap:6px}
.dots i{display:block;width:11px;height:5px;background:#aaa}
.dots i:first-child{background:#333}

/* category tiles */
.tiles{position:absolute;left:47px;top:759px;width:1106px;height:278px;display:flex}
.tile{flex:1;background:var(--black);position:relative;overflow:hidden;border-right:1px solid #333}
.tile:last-child{border-right:none}
.tile .ph{position:absolute;right:0;top:0;width:55%;height:100%;background:linear-gradient(90deg,#111,#4a4a4a 70%,#3a3a3a)}
.tile h3{position:absolute;left:31px;top:80px;font-size:22px;font-weight:400;line-height:1.15;color:#fff;z-index:2}
.tile h3 span{color:var(--orange)}
.tile p{position:absolute;left:31px;top:158px;width:270px;font-size:10px;color:#ddd;line-height:1.45;z-index:2}
.tile .btn{position:absolute;left:31px;top:222px;width:84px;height:28px;background:var(--orange);color:#fff;font-size:10.5px;font-weight:700;display:flex;align-items:center;justify-content:center;z-index:2}

/* products */
.new-products{position:absolute;left:0;top:1056px;width:1200px;height:851px;background:var(--grey-light)}
.section-head{position:absolute;left:47px;width:1106px;border-bottom:1px solid var(--line);padding-bottom:8px}
.section-head h2{font-size:22px;font-weight:400;color:#222}
.section-head h2 span{color:var(--orange)}
.sort{position:absolute;right:0;top:2px;width:88px;height:30px;border:1px solid #ccc;background:#fff;font-size:10px;color:#555;padding:8px 10px}
.grid{position:absolute;left:47px;width:1106px;display:grid;grid-template-columns:repeat(4,254px);column-gap:30px;row-gap:23px}
.card{background:#fff;border:1px solid #e2e2e2;height:356px;position:relative}
.card .ph{position:absolute;left:50px;top:20px;width:154px;height:160px;border-radius:6px}
.card .name{position:absolute;left:18px;top:218px;font-size:13px;color:#333}
.card .desc{position:absolute;left:18px;top:242px;width:220px;font-size:10.5px;color:var(--grey-text);line-height:1.4}
.card .price{position:absolute;left:18px;top:286px;font-size:18px;font-weight:600;color:var(--orange)}
.card .price s{font-size:12px;color:#999;font-weight:400;margin-right:10px}
.card .actions{position:absolute;left:0;bottom:0;width:100%;height:33px;display:flex}
.card .buy,.card .cart{flex:1;display:flex;align-items:center;justify-content:center;gap:8px;color:#fff;font-size:10.5px;font-weight:600}
.card .buy{background:var(--orange)}
.card .cart{background:var(--grey-btn)}

.feat .card{height:330px}
.feat .card .ph{top:22px;height:150px}
.feat .card .name{top:222px}
.feat .card .desc{top:246px}
.feat .preorder{position:absolute;left:18px;top:285px;width:114px;height:30px;border:1px solid var(--orange);color:var(--orange);font-size:10.5px;display:flex;align-items:center;justify-content:center}

/* promo banners */
.banners{position:absolute;left:47px;top:2358px;width:1106px;height:185px;display:flex;gap:20px}
.banner{flex:1;position:relative;overflow:hidden}
.banner .ph{position:absolute;inset:0}
.banner .frame{position:absolute;left:22px;top:18px;right:22px;bottom:18px;border:1px solid rgba(255,255,255,.5)}
.banner .label{position:absolute;left:0;top:72px;height:40px;padding:0 26px;background:var(--orange);color:#fff;font-size:19px;display:flex;align-items:center}

/* newsletter */
.newsletter{position:absolute;left:0;top:2569px;width:1200px;height:172px;background:var(--grey-band)}
.newsletter h3{position:absolute;left:187px;top:34px;font-size:35px;font-weight:300;color:var(--orange)}
.newsletter p{position:absolute;left:134px;top:93px;width:348px;font-size:12px;color:#555;line-height:1.5;text-align:center}
.newsletter .email{position:absolute;left:517px;top:37px;width:248px;height:40px;background:#fff;border:1px solid #ddd;font-size:11px;color:#999;padding:12px 14px;letter-spacing:.3px}
.newsletter .subscribe{position:absolute;left:517px;top:95px;width:248px;height:40px;background:#2b2b2b;color:#fff;font-size:12px;font-weight:600;display:flex;align-items:center;justify-content:center}
.newsletter .divider{position:absolute;left:821px;top:18px;width:1px;height:136px;background:#cfcfcf}
.socials{position:absolute;left:890px;top:36px;display:grid;grid-template-columns:repeat(3,48px);column-gap:20px;row-gap:9px}
.socials i{display:block;width:48px;height:48px;border-radius:50%;border:2px solid #bbb}
.socials i.red{border-color:var(--orange)}

/* guarantees */
.perks{position:absolute;left:0;top:2741px;width:1200px;height:138px;background:var(--orange);display:flex}
.perk{flex:1;display:flex;align-items:center;justify-content:flex-start;padding-left:80px;gap:22px;color:#fff;font-size:16px;font-weight:700;line-height:1.2;border-right:1px solid rgba(255,255,255,.35)}
.perk:last-child{border-right:none}

/* footer */
.footer{position:absolute;left:0;top:2879px;width:1200px;height:280px;background:var(--black);color:#aaa}
.fcol{position:absolute;top:70px}
.fcol h4{font-size:12px;font-weight:600;color:#fff;margin-bottom:20px;letter-spacing:.3px}
.fcol li{list-style:none;font-size:10.5px;line-height:22.6px;color:#9a9a9a}
.fcol .contact{display:flex;gap:12px;font-size:10.5px;line-height:1.6;margin-bottom:14px;color:#9a9a9a}
.bottom{position:absolute;left:0;top:3159px;width:1200px;height:73px;background:#111;border-top:1px solid #222}
.bottom .copy{position:absolute;left:52px;top:28px;font-size:10.5px;color:#888}
.bottom .mark{position:absolute;left:430px;top:20px;font-size:32px;font-weight:700;color:var(--mark-dim);line-height:1;letter-spacing:.5px}
.cards{position:absolute;right:47px;top:22px;display:flex;gap:8px}
.cards i{display:block;width:44px;height:28px;border-radius:3px;background:#ececec}
</style>
</head>
<body>

<div class="topbar">
  <div class="phone">
    <svg width="14" height="14" viewBox="0 0 24 24"><path fill="#e2492b" d="M6.6 10.8a15.1 15.1 0 0 0 6.6 6.6l2.2-2.2c.3-.3.7-.4 1-.2 1.1.4 2.3.6 3.6.6.6 0 1 .4 1 1V20c0 .6-.4 1-1 1A17 17 0 0 1 3 4c0-.6.4-1 1-1h3.5c.6 0 1 .4 1 1 0 1.3.2 2.5.6 3.6.1.3 0 .7-.2 1z"/></svg>
    1800 555 0142
  </div>
  <div class="links">
    <span class="hl">LOGIN/REGISTER</span><span class="sep">|</span>
    <span>MY ACCOUNT</span><span class="sep">|</span>
    <span>WISHLIST - 0</span><span class="sep">|</span>
    <span>SHOPPING TV - <span class="hl">$0.0</span></span>
  </div>
  <div class="checkout">CHECKOUT
    <svg width="14" height="12" viewBox="0 0 14 12"><path fill="#fff" d="M0 4h8V0l6 6-6 6V8H0z"/></svg>
  </div>
</div>

<header class="header">
  <div class="wordmark"><i></i>VOLTLINE SHOP</div>
  <div class="search"><div class="field">Enter keyword</div><div class="btn">SEARCH</div></div>
  <div class="currency">US Dollar $ &#8964;</div>
</header>

<nav class="nav">
  <ul>
    <li class="active">ABOUT US</li>
    <li>KITCHEN APPLIANCES</li>
    <li>COMPUTING</li>
    <li>MOBILE</li>
    <li>TV &amp; VIDEO</li>
    <li>SHIPPING</li>
    <li>RETURNS</li>
    <li>FAQ</li>
    <li>BLOG</li>
    <li>EVENTS</li>
    <li>CONTACT US</li>
  </ul>
</nav>

<section class="hero">
  <div class="ph-left" role="img" aria-label="Full HD television showing a flower scene with two smartphones in front"></div>
  <div class="ph-right" role="img" aria-label="Group of electronics: monitor, laptop, speakers and audio system"></div>
  <div class="copy">
    <div class="eyebrow">Electronics items <b>Offers</b></div>
    <div class="big">25% OFF</div>
    <div class="small">THE MARKED PRICE OFF</div>
    <div class="summer">SUMMER</div>
    <div class="hot">HOT OFFERS</div>
    <div class="shop">SHOP NOW</div>
  </div>
</section>
<div class="dots"><i></i><i></i><i></i><i></i></div>

<div class="tiles">
  <div class="tile">
    <div class="ph" role="img" aria-label="Smartphone on dark background"></div>
    <h3><span>MOBILE &amp;</span><br>COMPUTING</h3>
    <p>LOREM IPSUM DOLOR SIT AMET, EDIT CONSEC-TETUR ADIPISM EDITLOREM IPSUM DOLOR</p>
    <div class="btn">SHOP NOW</div>
  </div>
  <div class="tile">
    <div class="ph" role="img" aria-label="Refrigerator and washing machine"></div>
    <h3><span>KITCHEN</span><br>APPLIANCES</h3>
    <p>LOREM IPSUM DOLOR SIT AMET, EDIT CONSEC-TETUR ADIPISM EDITLOREM IPSUM DOLOR</p>
    <div class="btn">SHOP NOW</div>
  </div>
  <div class="tile">
    <div class="ph" role="img" aria-label="Television on a grass landscape" style="background:linear-gradient(180deg,#1d3f7a,#4d84c7 55%,#3e7d2a)"></div>
    <h3><span>TV &amp;</span><br>VIDEO</h3>
    <p>LOREM IPSUM DOLOR SIT AMET, EDIT CONSEC-TETUR ADIPISM EDITLOREM IPSUM DOLOR</p>
    <div class="btn">SHOP NOW</div>
  </div>
</div>

<section class="new-products">
  <div class="section-head" style="top:28px">
    <h2><span>NEW</span> PRODUCTS</h2>
    <div class="sort">SORT BY &#8964;</div>
  </div>
  <div class="grid" style="top:86px">
    <div class="card"><div class="ph" role="img" aria-label="Coffee machine" style="background:linear-gradient(160deg,#333,#d86a1e)"></div><div class="name">Name of the product</div><div class="desc">Lorem ipsum dolor sit amet conse ctetur adipiscing elit, sed do eusmodalique.</div><div class="price"><s>$35.00</s>$ 29.00</div><div class="actions"><div class="buy">&#10003; BUY NOW</div><div class="cart">&#9635; ADD TO CART</div></div></div>
    <div class="card"><div class="ph" role="img" aria-label="Flat screen television" style="background:linear-gradient(160deg,#111,#6a8aa8)"></div><div class="name">Name of the product</div><div class="desc">Lorem ipsum dolor sit amet conse ctetur adipiscing elit, sed do eusmodalique.</div><div class="price"><s>$35.00</s>$ 29.00</div><div class="actions"><div class="buy">&#10003; BUY NOW</div><div class="cart">&#9635; ADD TO CART</div></div></div>
    <div class="card"><div class="ph" role="img" aria-label="Compact digital camera" style="background:linear-gradient(160deg,#5a2f7a,#b58ad0)"></div><div class="name">Name of the product</div><div class="desc">Lorem ipsum dolor sit amet conse ctetur adipiscing elit, sed do eusmodalique.</div><div class="price"><s>$35.00</s>$ 29.00</div><div class="actions"><div class="buy">&#10003; BUY NOW</div><div class="cart">&#9635; ADD TO CART</div></div></div>
    <div class="card"><div class="ph" role="img" aria-label="Top-loading washing machine" style="background:linear-gradient(160deg,#c8c8c8,#c2596e)"></div><div class="name">Name of the product</div><div class="desc">Lorem ipsum dolor sit amet conse ctetur adipiscing elit, sed do eusmodalique.</div><div class="price"><s>$35.00</s>$ 29.00</div><div class="actions"><div class="buy">&#10003; BUY NOW</div><div class="cart">&#9635; ADD TO CART</div></div></div>
    <div class="card"><div class="ph" role="img" aria-label="Smartphone" style="background:linear-gradient(160deg,#222,#6a6a6a)"></div><div class="name">Name of the product</div><div class="desc">Lorem ipsum dolor sit amet conse ctetur adipiscing elit, sed do eusmodalique.</div><div class="price"><s>$35.00</s>$ 29.00</div><div class="actions"><div class="buy">&#10003; BUY NOW</div><div class="cart">&#9635; ADD TO CART</div></div></div>
    <div class="card"><div class="ph" role="img" aria-label="Induction cooktop" style="background:linear-gradient(160deg,#1c2430,#8b99a8)"></div><div class="name">Name of the product</div><div class="desc">Lorem ipsum dolor sit amet conse ctetur adipiscing elit, sed do eusmodalique.</div><div class="price"><s>$35.00</s>$ 29.00</div><div class="actions"><div class="buy">&#10003; BUY NOW</div><div class="cart">&#9635; ADD TO CART</div></div></div>
    <div class="card"><div class="ph" role="img" aria-label="Hi-fi music system with speakers" style="background:linear-gradient(160deg,#0e0e0e,#555)"></div><div class="name">Name of the product</div><div class="desc">Lorem ipsum dolor sit amet conse ctetur adipiscing elit, sed do eusmodalique.</div><div class="price"><s>$35.00</s>$ 29.00</div><div class="actions"><div class="buy">&#10003; BUY NOW</div><div class="cart">&#9635; ADD TO CART</div></div></div>
    <div class="card"><div class="ph" role="img" aria-label="Video projector" style="background:linear-gradient(160deg,#111,#4c4c4c)"></div><div class="name">Name of the product</div><div class="desc">Lorem ipsum dolor sit amet conse ctetur adipiscing elit, sed do eusmodalique.</div><div class="price"><s>$35.00</s>$ 29.00</div><div class="actions"><div class="buy">&#10003; BUY NOW</div><div class="cart">&#9635; ADD TO CART</div></div></div>
  </div>
</section>

<section class="feat">
  <div class="section-head" style="top:1936px">
    <h2><span>FEATURED</span> PRODUCTS</h2>
  </div>
  <div class="grid" style="top:1993px">
    <div class="card"><div class="ph" role="img" aria-label="Espresso machine" style="background:linear-gradient(160deg,#1a1a1a,#8a8a8a)"></div><div class="name">Product Name Here</div><div class="desc">Lorem ipsum dolor sit amet conse ctetur adipiscing elit, sed do eusmodalique.</div><div class="preorder">PRE-ORDER NOW</div></div>
    <div class="card"><div class="ph" role="img" aria-label="Gaming desktop computer" style="background:linear-gradient(160deg,#0f0f0f,#2f5bb0)"></div><div class="name">Product Name Here</div><div class="desc">Lorem ipsum dolor sit amet conse ctetur adipiscing elit, sed do eusmodalique.</div><div class="preorder">PRE-ORDER NOW</div></div>
    <div class="card"><div class="ph" role="img" aria-label="Wall-mounted air conditioner" style="background:linear-gradient(160deg,#ececec,#7a1c2c)"></div><div class="name">Product Name Here</div><div class="desc">Lorem ipsum dolor sit amet conse ctetur adipiscing elit, sed do eusmodalique.</div><div class="preorder">PRE-ORDER NOW</div></div>
    <div class="card"><div class="ph" role="img" aria-label="Refrigerator" style="background:linear-gradient(160deg,#6a1234,#c23a6e)"></div><div class="name">Product Name Here</div><div class="desc">Lorem ipsum dolor sit amet conse ctetur adipiscing elit, sed do eusmodalique.</div><div class="preorder">PRE-ORDER NOW</div></div>
  </div>
</section>

<div class="banners">
  <div class="banner"><div class="ph" role="img" aria-label="Flat lay of accessories: wallet, headphones and gadgets" style="background:linear-gradient(135deg,#1c1c1c,#3d3d3d)"></div><div class="frame"></div><div class="label">ACCESORIES</div></div>
  <div class="banner"><div class="ph" role="img" aria-label="Hands using tablets and devices on a table" style="background:linear-gradient(135deg,#3a2a1f,#8a6a4a)"></div><div class="frame"></div><div class="label">SUMMER OFFER</div></div>
  <div class="banner"><div class="ph" role="img" aria-label="Kitchen with home appliances" style="background:linear-gradient(135deg,#0e1a2a,#3a4a5c)"></div><div class="frame"></div><div class="label">HOME APPLIANCES</div></div>
</div>

<section class="newsletter">
  <h3>Newsletter Sign Up</h3>
  <p>Lorem ipsum dolor sit amet conse ctetur adipiscing elit, sed do eius-mod tempor incididunt ut labore et dolore magna aliqua.</p>
  <div class="email">ENTER YOUR EMAIL ADDRESS</div>
  <div class="subscribe">SUBSCRIBE</div>
  <div class="divider"></div>
  <div class="socials" aria-label="Social network links">
    <i></i><i class="red"></i><i class="red"></i>
    <i class="red"></i><i class="red"></i><i class="red"></i>
  </div>
</section>

<section class="perks">
  <div class="perk">
    <svg width="40" height="40" viewBox="0 0 24 24"><path fill="#fff" d="M2 10h4v11H2zm6 11h9c.8 0 1.5-.5 1.8-1.2l2.6-6.4c.4-1.1-.4-2.4-1.6-2.4h-5.4l.9-4.3c.2-.9-.5-1.7-1.4-1.7L8 10z"/></svg>
    <div>SATISFACTION<br>100% GUARANTEED</div>
  </div>
  <div class="perk">
    <svg width="48" height="36" viewBox="0 0 32 24"><path fill="#fff" d="M1 3h19v14H1zm20 4h6l4 5v5h-10z"/><circle cx="7" cy="19" r="3" fill="#fff" stroke="#e2492b" stroke-width="1.5"/><circle cx="25" cy="19" r="3" fill="#fff" stroke="#e2492b" stroke-width="1.5"/></svg>
    <div>FREE SHIPPING<br>ON ORDERS OVER $99</div>
  </div>
  <div class="perk">
    <svg width="40" height="40" viewBox="0 0 24 24"><path fill="none" stroke="#fff" stroke-width="3" d="M19 9a8 8 0 0 0-14-2M5 15a8 8 0 0 0 14 2"/><path fill="#fff" d="M3 2v7h7zM21 22v-7h-7z"/></svg>
    <div>7 DAY<br>EASY RETURN</div>
  </div>
</section>

<footer class="footer">
  <div class="fcol" style="left:54px"><h4>INFORMATION</h4><ul><li>ABOUT US</li><li>CUSTOMER SERVICE</li><li>PRIVACY POLICY</li><li>SEARCH TERMS</li><li>ORDERS AND RETURNS</li><li>CONTACT US</li></ul></div>
  <div class="fcol" style="left:323px"><h4>WHY BUY FROM US</h4><ul><li>SHIPPING &amp; RETURNS</li><li>SECURE SHOPPING</li><li>INTERNATIONAL SHIPPING</li><li>AFFILIATES</li><li>GROUP SALES</li></ul></div>
  <div class="fcol" style="left:625px"><h4>MY ACCOUNT</h4><ul><li>SIGN IN</li><li>VIEW CART</li><li>MY WISHLIST</li><li>TRACK MY ORDER</li><li>HELP</li></ul></div>
  <div class="fcol" style="left:868px"><h4>CONTACTS</h4>
    <div class="contact"><svg width="12" height="14" viewBox="0 0 12 16"><path fill="#9a9a9a" d="M6 0a6 6 0 0 0-6 6c0 4.5 6 10 6 10s6-5.5 6-10a6 6 0 0 0-6-6zm0 8.5A2.5 2.5 0 1 1 6 3.5a2.5 2.5 0 0 1 0 5z"/></svg><span>12 HARBOR LANE, EASTFIELD E14 7QT<br>P. O BOX 40218, COUNTRY</span></div>
    <div class="contact"><svg width="12" height="12" viewBox="0 0 24 24"><path fill="#9a9a9a" d="M6.6 10.8a15.1 15.1 0 0 0 6.6 6.6l2.2-2.2c.3-.3.7-.4 1-.2 1.1.4 2.3.6 3.6.6.6 0 1 .4 1 1V20c0 .6-.4 1-1 1A17 17 0 0 1 3 4c0-.6.4-1 1-1h3.5c.6 0 1 .4 1 1 0 1.3.2 2.5.6 3.6.1.3 0 .7-.2 1z"/></svg><span>CALL US: (800) 555-0199</span></div>
    <div class="contact"><svg width="13" height="10" viewBox="0 0 16 12"><path fill="#9a9a9a" d="M0 0h16v12H0zm1.5 1.5L8 6.5l6.5-5z"/></svg><span>EMAIL HELLO@VOLTLINE.EXAMPLE</span></div>
  </div>
</footer>

<div class="bottom">
  <div class="copy">All Rights Reserved. Copyrights @ 2015</div>
  <div class="mark">VOLTLINE SHOP</div>
  <div class="cards" aria-label="Accepted payment cards"><i></i><i></i><i></i></div>
</div>

</body>
</html>
```